Builder of high-end, expensive tables and other furniture

Build a website that represents what we do. I want a luxury feel that appeals to those who can afford our products. We build very high end tables and other furniture using trees that have fallen or are standing dead. We never cut living trees. Trees are harvested, milled, and kiln dried. Then that lumber is meticulously turned into fine furniture using the best equipment. Our furniture prices range from $1,000-$20,000.

Trying to figure out how to raise my spend.

```html
<!DOCTYPE html>
<html lang="en">
<head>
<meta charset="utf-8">
<title>Heartwood Atelier — Fine Furniture from Fallen Trees</title>
<link href="https://fonts.googleapis.com/css2?family=EB+Garamond:ital,wght@0,400;0,500;1,400&family=Poppins:wght@400;500;600&display=swap" rel="stylesheet">
<style>
:root{
  --ink:#1d1b19;
  --body:#55504a;
  --muted:#9a948c;
  --line:#d9d3c8;
  --paper:#ffffff;
  --footer:#f2f0ec;
  --accent:#e8385a;
  --white:#ffffff;
  --brand:#cf6a2a;
}
*{box-sizing:border-box;margin:0;padding:0}
html,body{width:1200px;height:4886px;overflow:hidden;background:var(--paper)}
body{position:relative;font-family:"EB Garamond",Georgia,serif;color:var(--body)}
.abs{position:absolute}
.caps{font-family:"Poppins",Arial,sans-serif;text-transform:uppercase;letter-spacing:.22em;font-weight:500}
.photo{position:absolute}

/* hero */
.hero{position:absolute;left:0;top:0;width:1200px;height:552px}
.brand{position:absolute;left:70px;top:56px;font-family:"EB Garamond",serif;font-size:40px;color:var(--white);display:flex;align-items:center;gap:12px;white-space:nowrap}
.brand-dot{width:13px;height:13px;border-radius:50%;background:currentColor;flex:none}
.nav a{position:absolute;top:49px;font-size:9.5px;color:var(--white);text-decoration:none;white-space:nowrap}
.menu-icon{position:absolute;left:1080px;top:48px;width:34px}
.menu-icon i{display:block;height:1px;background:var(--white);margin-bottom:6px}
.hero-kicker{left:0;width:1200px;top:210px;text-align:center;color:var(--white);font-size:12px}
.hero-title{left:0;width:1200px;top:234px;text-align:center;color:var(--white);font-style:italic;font-weight:400;font-size:37px;line-height:42px}
.btn{display:block;border:1px solid currentColor;text-align:center;font-size:9.5px}
.hero-btn{left:537px;top:350px;width:123px;height:38px;line-height:36px;color:var(--white)}

/* split sections */
.eyebrow{font-size:15px;color:var(--ink);letter-spacing:.26em;font-weight:600;white-space:nowrap}
.copy{font-size:15.5px;line-height:22px;color:var(--body)}
.btn-dark{color:var(--ink);border-color:#b8b1a6;height:37px;line-height:35px}

.acc-head{left:75px;font-size:10px;color:var(--ink);white-space:nowrap}
.acc-line{left:75px;width:425px;height:1px;background:var(--line)}
.acc-body{left:90px;top:1563px;width:370px;font-size:15.5px;line-height:22px;color:var(--body)}

.tiles{left:0;top:2027px;width:1200px;height:400px;display:flex}
.tile{position:relative;width:400px;height:400px}
.tile .caps{position:absolute;left:0;right:0;top:192px;text-align:center;color:var(--white);font-size:12px}
.side-tool{left:1170px;width:30px;height:30px}

.links{font-size:9.5px;color:var(--muted)}
.links div{text-decoration:underline;margin-bottom:11px;white-space:nowrap}

/* testimonial */
.quote{left:0;width:1200px;text-align:center}
.quote-text{font-style:italic;font-size:31px;line-height:36px;color:var(--ink)}
.arrow{top:3462px}

/* cards */
.card{top:3667px;width:360px;height:513px}
.card .tag{position:absolute;left:13px;top:13px;background:var(--white);padding:5px 14px;font-size:9px;color:var(--muted)}
.card .label{position:absolute;left:0;bottom:0;width:338px;height:52px;background:var(--white);padding:20px 0 0 18px;font-size:11px;color:var(--ink)}

/* footer */
.footer{left:0;top:4372px;width:1200px;height:514px;background:var(--footer)}
.news-title{left:0;width:1200px;top:4458px;text-align:center;font-size:17px;color:var(--ink);letter-spacing:.28em;font-weight:600}
.news-input{left:405px;top:4500px;width:287px;height:38px;border:1px solid #cfc8bc;font-size:12px;padding:10px 15px;color:var(--muted)}
.news-btn{left:692px;top:4500px;width:103px;height:38px;border:1px solid #cfc8bc;border-left:none;text-align:center;line-height:37px;font-size:9px;color:var(--ink)}
.fcol{top:4608px;width:200px}
.fcol h4{font-size:11px;color:var(--ink);margin-bottom:14px;font-weight:600}
.fcol div{font-size:9px;color:var(--muted);line-height:20px;letter-spacing:.2em;white-space:nowrap}
.footer-brand{left:770px;top:4660px;font-size:34px;color:var(--brand);display:flex;align-items:center;gap:10px;white-space:nowrap}
</style>
</head>
<body>

<header class="hero">
  <div class="photo" role="img" aria-label="Bright dining room with a walnut table, wooden chairs and a paper pendant lamp" style="inset:0;background:linear-gradient(120deg,#bfb2a0 0%,#9c8a75 30%,#6e5a44 58%,#d6d2cb 85%,#c9c4bb 100%)"></div>
  <div class="brand"><span class="brand-dot"></span>Heartwood Atelier</div>
  <nav class="nav caps">
    <a style="left:612px">Home</a><a style="left:701px">Pages</a><a style="left:789px">Portfolio</a><a style="left:914px">Blog</a><a style="left:996px">Shop</a>
  </nav>
  <div class="menu-icon"><i></i><i></i><i></i></div>
  <div class="abs caps hero-kicker">Reclaimed</div>
  <h1 class="abs hero-title">Heirloom tables crafted only from fallen<br>and standing-dead trees.</h1>
  <div class="abs caps btn hero-btn">View more</div>
</header>

<section>
  <div class="photo" role="img" aria-label="Round white pedestal table with two wooden chairs beneath a globe pendant by tall windows" style="left:75px;top:654px;width:525px;height:708px;background:linear-gradient(180deg,#8e8a83 0%,#c9c3b8 45%,#a67a4c 100%)"></div>
  <div class="abs caps eyebrow" style="left:714px;top:900px">Furniture</div>
  <p class="abs copy" style="left:714px;top:928px;width:390px">Every piece begins with a tree that has fallen or stood dead in the forest. We never cut a living tree. Each log is harvested, milled and slowly kiln dried before it reaches our bench.</p>
  <div class="abs caps btn btn-dark" style="left:714px;top:1040px;width:119px">View more</div>
</section>

<section>
  <div class="abs caps acc-head" style="top:1512px">– Our philosophy</div>
  <div class="abs acc-line" style="top:1545px"></div>
  <p class="abs acc-body">We never cut living trees. Only fallen and standing-dead timber is harvested, so each table carries a history.</p>
  <div class="abs caps acc-head" style="top:1669px">+ From forest to mill</div>
  <div class="abs acc-line" style="top:1700px"></div>
  <div class="abs caps acc-head" style="top:1724px">+ Kiln dried, slow made</div>
  <div class="abs acc-line" style="top:1756px"></div>
  <div class="abs caps acc-head" style="top:1779px">+ Built for generations</div>
  <div class="abs acc-line" style="top:1811px"></div>
  <div class="photo" role="img" aria-label="Close view of a solid oak dining table with wishbone chairs" style="left:600px;top:1450px;width:535px;height:472px;background:linear-gradient(150deg,#8a7660 0%,#c8a97c 40%,#b8925f 70%,#6d5a45 100%)"></div>
</section>

<section class="abs tiles">
  <div class="tile" role="img" aria-label="Kitchen with a long wooden table, grey chairs and blue rug" style="background:linear-gradient(180deg,#d8d4cc 0%,#a17a52 55%,#2c4d86 100%)"><span class="caps">Kitchen</span></div>
  <div class="tile" role="img" aria-label="Bathroom with white vanity top over a walnut cabinet" style="background:linear-gradient(180deg,#e4e2de 0%,#d2cfca 60%,#6b3f22 100%)"><span class="caps">Bathroom</span></div>
  <div class="tile" role="img" aria-label="Living room with a wood-clad fireplace, sofa and low table" style="background:linear-gradient(180deg,#e0ddd8 0%,#8c6a44 45%,#5a5550 100%)"><span class="caps">Living room</span></div>
</section>
<div class="abs side-tool" style="top:2317px;background:var(--accent)"></div>
<div class="abs side-tool" style="top:2353px;background:var(--white)"></div>

<section>
  <div class="photo" role="img" aria-label="White kitchen cabinets over a blue hexagon tile backsplash" style="left:75px;top:2540px;width:525px;height:710px;background:linear-gradient(180deg,#efece6 0%,#e9e5de 35%,#5c6f8a 55%,#e7e4de 70%,#e2ded7 100%)"></div>
  <div class="abs caps eyebrow" style="left:714px;top:2788px">Craft and value</div>
  <p class="abs copy" style="left:714px;top:2815px;width:390px">Pieces range from $1,000 to $20,000, each made to order on precision equipment and finished by hand for homes that expect the finest.</p>
  <div class="abs caps links" style="left:714px;top:2898px">
    <div>Kitchen and dining rooms</div><div>Bedrooms and living rooms</div><div>Bathrooms and laundry rooms</div><div>Work spaces and gardens</div>
  </div>
  <div class="abs caps btn btn-dark" style="left:714px;top:3021px;width:124px">View more</div>
</section>

<section>
  <div class="abs quote caps" style="top:3380px;font-size:11px;color:var(--ink);font-weight:600">Client words:</div>
  <blockquote class="abs quote quote-text" style="top:3400px">Our table began as a walnut felled by a storm.<br>It is the heart of our home now, and it will<br>outlast every one of us.</blockquote>
  <div class="abs quote" style="top:3528px;font-size:15px">Elias Marlow</div>
  <svg class="abs arrow" style="left:50px" width="22" height="38" viewBox="0 0 22 38"><path d="M20 1 2 19l18 18" fill="none" stroke="#333" stroke-width="1.5"/></svg>
  <svg class="abs arrow" style="left:1128px" width="22" height="38" viewBox="0 0 22 38"><path d="M2 1l18 18L2 37" fill="none" stroke="#333" stroke-width="1.5"/></svg>
</section>

<section>
  <article class="abs card" role="img" aria-label="Bright white kitchen with a person reading by the counter" style="left:55px;background:linear-gradient(180deg,#2a2a2a 0%,#e6e3de 30%,#d9d6d0 70%,#8a6a48 100%)">
    <span class="tag caps">Art, design</span><div class="label caps">Kitchen</div>
  </article>
  <article class="abs card" role="img" aria-label="Double bathroom vanity with round mirrors and light wood cabinet" style="left:420px;background:linear-gradient(180deg,#cfcbc4 0%,#e7e6e2 40%,#d8c59d 70%,#3f5a5a 100%)">
    <span class="tag caps">Art, design</span><div class="label caps">Baths</div>
  </article>
  <article class="abs card" role="img" aria-label="Living room mantel with a blue and white vase and a wall lamp" style="left:787px;background:linear-gradient(90deg,#dcd7cd 0%,#ece8e0 45%,#e9e4db 70%,#5e4934 100%)">
    <span class="tag caps">Art, design</span><div class="label caps">Living</div>
  </article>
</section>

<footer>
  <div class="abs footer"></div>
  <h2 class="abs caps news-title">Join our newsletter</h2>
  <div class="abs news-input">Your e-mail*</div>
  <div class="abs caps news-btn">Sign up</div>
  <div class="abs fcol caps" style="left:90px"><h4>Information</h4><div>About us</div><div>Our team</div><div>Contact us</div><div>Pricing plans</div></div>
  <div class="abs fcol caps" style="left:298px"><h4>Social</h4><div>Pictora</div><div>Chirpline</div><div>Portfolia</div><div>Pinwall</div><div>Shotbook</div></div>
  <div class="abs fcol caps" style="left:507px;width:260px"><h4>Contact</h4><div>Headquarters</div><div>Tel + 45 70 40 18 26</div><div>info@heartwoodatelier.dk</div><div>Tømrervej 14, 2450</div><div>København, DK</div></div>
  <div class="abs footer-brand"><span class="brand-dot"></span>Heartwood Atelier</div>
</footer>

</body>
</html>
```